Engineering Consultant Business Card

I'm starting a new business as a high-end engineering consultant in a niche field. I've attached the jpg for my logo plus the branding guideline document that I've been following. You can see my business website here: www.tarvikworks.com
I'd like a business card that has the logo on one side, then the other side has (in any order): Tarvik Works, Inc.
Dana Whitlock
President and Chief EMC Engineer
www.tarvikworks.com
dana@tarvikworks.com
Optional: motto "We will solve your EMC problems as early as possible—ideally before they even start."
I'm not planning on including a phone number
Target Market(s)
Businesses, especially makers of electronics hardware
Industry/Entity Type
Electrical engineering
Contact Information for Business Card
Company name, my name, website, email

```html
<!DOCTYPE html>
<html lang="en">
<head>
<meta charset="utf-8">
<title>Tarvik Works, Inc. — Business Card</title>
<link rel="stylesheet" href="https://fonts.googleapis.com/css2?family=Public+Sans:wght@400;500;700&display=swap">
<style>
  :root {
    --navy: #30469a;
    --ink: #24346f;
    --sky: #52aecf;
    --paper: #ffffff;
    --stage-grey: #e5e5e5;
    --text: #111111;
  }
  * { margin: 0; padding: 0; box-sizing: border-box; }
  html, body { width: 1200px; height: 1200px; overflow: hidden; }
  body {
    font-family: "Public Sans", Arial, sans-serif;
    background: linear-gradient(to right, var(--navy) 0 619px, var(--stage-grey) 619px 100%);
    position: relative;
  }
  .card {
    position: absolute;
    left: 230px;
    width: 739px;
    height: 422px;
    background: var(--paper);
    overflow: hidden;
  }
  .card--front { top: 148px; }
  .card--back { top: 630px; }
  .card-shapes { position: absolute; inset: 0; width: 100%; height: 100%; display: block; }
  .shape-navy { fill: var(--navy); }
  .shape-sky { fill: var(--sky); }

  .company-name {
    position: absolute;
    right: 51px;
    top: 236px;
    top: 97px;
    font-size: 56px;
    font-weight: 700;
    line-height: 1;
    letter-spacing: -0.5px;
    color: var(--ink);
  }
  .company-name .accent { color: var(--sky); }

  .contact-list {
    position: absolute;
    right: 48px;
    top: 267px;
    list-style: none;
  }
  .contact-item {
    display: flex;
    align-items: center;
    justify-content: flex-end;
    gap: 8px;
  }
  .contact-item + .contact-item { margin-top: 16px; }
  .contact-item--person { margin-bottom: 6px; }
  .person-name {
    font-size: 20px;
    font-weight: 700;
    color: var(--navy);
    line-height: 1.05;
    text-align: right;
  }
  .person-role {
    font-size: 11px;
    font-weight: 500;
    color: var(--text);
    text-align: right;
    line-height: 1.2;
  }
  .contact-text { font-size: 11px; color: var(--text); }
  .contact-icon { width: 30px; height: 30px; flex: none; display: block; }
  .contact-icon .icon-fill { fill: var(--navy); }
  .contact-icon .icon-line { fill: none; stroke: var(--paper); stroke-width: 1.4; }

  .brand-mark {
    position: absolute;
    left: 30px;
    top: 195px;
    display: flex;
    align-items: center;
    gap: 14px;
  }
  .brand-mark .brand-dot {
    width: 46px; height: 46px;
    border-radius: 50%;
    background: var(--navy);
  }
  .brand-mark .brand-name {
    font-size: 40px;
    font-weight: 700;
    color: var(--navy);
    line-height: 1;
  }
</style>
</head>
<body>

<section class="card card--front" aria-label="Business card front">
  <svg class="card-shapes" viewBox="0 0 1189 679" preserveAspectRatio="none" aria-hidden="true">
    <path class="shape-navy" d="M255 0 H529 V95 A417 415 0 0 1 112 510 H0 V238 H112 A143 143 0 0 0 255 95 Z"/>
    <path class="shape-sky" d="M0 510 H112 C250 510 370 575 447 679 H0 Z"/>
    <path class="shape-navy" d="M864 0 C950 62 1060 96 1189 81 V0 Z"/>
  </svg>

  <h1 class="company-name">Tarvik <span class="accent">Works</span></h1>

  <ul class="contact-list">
    <li class="contact-item contact-item--person">
      <div>
        <p class="person-name">Inc. Dana Whitlock</p>
        <p class="person-role">President and Chief EMC Engineer</p>
      </div>
      <svg class="contact-icon" viewBox="0 0 30 30" aria-hidden="true">
        <circle class="icon-fill" cx="15" cy="8" r="6.5"/>
        <path class="icon-fill" d="M3 23 C3 17 9 15 11 15 C13 18 17 18 19 15 C21 15 27 17 27 23 C27 28 3 28 3 23 Z"/>
      </svg>
    </li>
    <li class="contact-item">
      <span class="contact-text">www.tarvikworks.com</span>
      <svg class="contact-icon" viewBox="0 0 30 30" aria-hidden="true">
        <path class="icon-fill" d="M1 15 L8 7 C12 3 18 3 22 7 L29 15 L22 23 C18 27 12 27 8 23 Z"/>
        <circle class="icon-line" cx="15" cy="15" r="6"/>
        <path class="icon-line" d="M9 15 H21 M15 9 V21 M10 12 H20 M10 18 H20"/>
      </svg>
    </li>
    <li class="contact-item">
      <span class="contact-text">dana@tarvikworks.com</span>
      <svg class="contact-icon" viewBox="0 0 30 30" aria-hidden="true">
        <path class="icon-fill" d="M1 15 L8 7 C12 3 18 3 22 7 L29 15 L22 23 C18 27 12 27 8 23 Z"/>
        <rect class="icon-line" x="9" y="10.5" width="12" height="9"/>
        <path class="icon-line" d="M9 10.5 L15 16 L21 10.5"/>
      </svg>
    </li>
  </ul>
</section>

<section class="card card--back" aria-label="Business card back">
  <svg class="card-shapes" viewBox="0 0 1189 679" preserveAspectRatio="none" aria-hidden="true">
    <path class="shape-navy" d="M0 0 H249 C180 75 100 120 0 135 Z"/>
    <path class="shape-sky" d="M744 0 C820 105 940 169 1078 169 H1189 V0 Z"/>
    <path class="shape-navy" d="M661 679 V584 A417 415 0 0 1 1078 169 H1189 V441 H1078 A144 143 0 0 0 934 584 V679 Z"/>
  </svg>

  <div class="brand-mark">
    <span class="brand-dot"></span>
    <span class="brand-name">Tarvik Works</span>
  </div>
</section>

</body>
</html>
```